Ferris Contracting LLC Business Card Design

I am looking for a creative and unique business card design. We are a commercial construction general contractor. With the name "FERRIS" Contracting, I am hoping to see some neat designs that correlate with the name.

```html
<!DOCTYPE html>
<html lang="en">
<head>
<meta charset="utf-8">
<title>Ferris Contracting LLC – Business Card</title>
<link rel="stylesheet" href="https://fonts.googleapis.com/css2?family=Arimo:wght@400;700&display=swap">
<style>
  :root {
    --stage: #5a5a5a;
    --card-dark: #2f2f2f;
    --brand-blue: #2a93d5;
    --blue-deep: #0e72b8;
    --blue-light: #33a6de;
    --text-light: #f2f2f2;
    --text-muted: #b5b5b5;
    --divider: #6a6a6a;
  }
  * { margin: 0; padding: 0; box-sizing: border-box; }
  html, body {
    width: 1200px; height: 1200px; overflow: hidden;
    background: var(--stage);
    font-family: "Arimo", Arial, sans-serif;
  }
  .card { position: absolute; overflow: hidden; }

  .card-front {
    left: 266px; top: 158px; width: 689px; height: 393px;
    background: var(--card-dark);
  }
  .card-back {
    left: 260px; top: 651px; width: 692px; height: 395px;
    background: radial-gradient(ellipse at 50% 40%, var(--blue-light) 0%, var(--brand-blue) 40%, var(--blue-deep) 100%);
  }

  .wordmark {
    position: absolute;
    font-weight: 700;
    text-align: center;
    white-space: nowrap;
    letter-spacing: 1px;
  }
  .wordmark span { display: block; }
  .card-front .wordmark {
    left: 85px; top: 150px; width: 254px;
    font-size: 28px; line-height: 32px; color: var(--brand-blue);
  }
  .card-back .wordmark {
    left: 0; top: 150px; width: 692px;
    font-size: 44px; line-height: 50px; color: #ffffff;
  }

  .divider {
    position: absolute; left: 358px; top: 81px;
    width: 1px; height: 202px; background: var(--divider);
  }

  .contact { position: absolute; left: 379px; top: 92px; color: var(--text-light); }
  .contact-name {
    font-size: 26px; font-weight: 700; color: var(--brand-blue);
    line-height: 30px; letter-spacing: 0.3px;
  }
  .contact-role { font-size: 15px; color: var(--text-muted); line-height: 20px; }
  .contact-address { margin-top: 18px; font-size: 16.5px; line-height: 21px; }
  .contact-lines { margin-top: 14px; list-style: none; }
  .contact-lines li {
    display: flex; align-items: center;
    font-size: 16.5px; line-height: 20.5px;
  }
  .contact-lines svg { width: 14px; height: 14px; margin-right: 10px; margin-left: 2px; flex: none; }

  .footer-bands { position: absolute; left: 0; top: 360px; width: 689px; height: 33px; }
  .footer-url {
    position: absolute; left: 438px; top: 366px;
    font-size: 16.5px; color: #ffffff; line-height: 20px;
  }
</style>
</head>
<body>

<section class="card card-front">
  <div class="wordmark"><span>FERRIS</span><span>CONTRACTING</span></div>

  <div class="divider"></div>

  <div class="contact">
    <div class="contact-name">DANIEL REYES</div>
    <div class="contact-role">President</div>
    <div class="contact-address">4120 Alder Ridge Road<br>Westbrook, Canada 58210</div>
    <ul class="contact-lines">
      <li>
        <svg viewBox="0 0 24 24" aria-hidden="true"><path fill="#2a93d5" d="M6.6 10.8a15.1 15.1 0 0 0 6.6 6.6l2.2-2.2c.3-.3.7-.4 1-.2 1.1.4 2.3.6 3.6.6.6 0 1 .4 1 1V20c0 .6-.4 1-1 1A17 17 0 0 1 3 4c0-.6.4-1 1-1h3.5c.6 0 1 .4 1 1 0 1.3.2 2.5.6 3.6.1.3 0 .7-.2 1z"/></svg>
        555-214-7730
      </li>
      <li>
        <svg viewBox="0 0 24 24" aria-hidden="true"><rect x="6" y="1.5" width="12" height="21" rx="2" fill="none" stroke="#2a93d5" stroke-width="2.4"/><rect x="10" y="18" width="4" height="1.6" fill="#2a93d5"/></svg>
        555-839-1062
      </li>
      <li>
        <svg viewBox="0 0 24 24" aria-hidden="true"><rect x="2" y="5" width="20" height="14" fill="#2a93d5"/><path d="M2 5l10 8 10-8" fill="none" stroke="#2f2f2f" stroke-width="2"/></svg>
        info@ferriscontracting.com
      </li>
    </ul>
  </div>

  <svg class="footer-bands" viewBox="0 0 689 33" preserveAspectRatio="none" aria-hidden="true">
    <defs>
      <linearGradient id="steel" x1="0" y1="0" x2="0" y2="1">
        <stop offset="0" stop-color="#e6e6e6"/>
        <stop offset="0.5" stop-color="#bdbdbd"/>
        <stop offset="1" stop-color="#8f8f8f"/>
      </linearGradient>
    </defs>
    <polygon points="0,4 397,4 390,17 0,17" fill="url(#steel)"/>
    <polygon points="0,18 689,18 689,33 0,33" fill="#2a93d5"/>
    <polygon points="404,1 689,1 689,20 395,20 398,8" fill="#2a93d5"/>
  </svg>
  <div class="footer-url">www.ferriscontracting.com</div>
</section>

<section class="card card-back">
  <div class="wordmark"><span>FERRIS</span><span>CONTRACTING</span></div>
</section>

</body>
</html>
```